Process Roadmap for Interior Design Firm

We are looking to ramp up the design appeal of our current process roadmap to be very visually interesting, while staying informative and descriptive about our process.

Target Market(s)

In-house Clients

Industry/Entity Type

Interior Design Firm focused on sustainable and holistic design.

Other font styles liked:
• raleway

Requirements
Must have
• 1.) it would be nice if the graphic provided a more clear indication of the “journey” from one step to the next, so that there was a clear sense of the progression (such that we are directing the viewer) 2.). We would want it to fit on an 8.5”x11” page (the page could be horizontal when we have the Calm Compass formatted out with the testimonials) (in addition to the testimonials, we may also want to have the detailed descriptions of each step of the process presented below the graphic, so that the graphic is cleaner) 3.) ideally the graphic is clear and simple enough to also be used on our Bi-Weekly Client Updates, which will be typed updates for clients re their project budgets, schedule and scope. The Calm Compass graphic (without all the testimonials) would be at the end of the update, and would fit on the page horizontally at the bottom, perhaps in a space which is 7.5”w x 4”h or so.
Should not have
• bold or bright colors. Natural neutrals are preferred, such as the ones featured on the provided graphic.

```html
<!DOCTYPE html>
<html lang="en">
<head>
<meta charset="utf-8">
<title>NLD Calm Compass</title>
<link rel="stylesheet" href="https://fonts.googleapis.com/css2?family=Roboto:wght@300;400;700&display=swap">
<style>
  :root {
    --tan: #c2b59b;
    --tan-dark: #a99a7c;
    --heading: #b5a686;
    --body-text: #a6977a;
    --icon: #c9bca3;
    --icon-light: #e2dbcd;
    --paper: #ffffff;
  }
  * { margin: 0; padding: 0; box-sizing: border-box; }
  html, body { width: 1200px; height: 927px; overflow: hidden; background: var(--paper); }
  body { font-family: "Roboto", Arial, sans-serif; color: var(--body-text); }
  .page { position: relative; width: 1200px; height: 927px; overflow: hidden; }

  .architecture-backdrop {
    position: absolute; left: 540px; top: 36px; width: 660px; height: 656px;
    background: radial-gradient(ellipse at 75% 35%, rgba(194,181,155,0.16), rgba(194,181,155,0.05) 55%, rgba(255,255,255,0) 80%);
  }

  .top-band { position: absolute; left: 0; top: 0; width: 1200px; height: 70px; }
  .page-title {
    position: absolute; left: 0; top: 22px; width: 1200px; text-align: center;
    font-weight: 700; font-size: 25px; color: var(--paper); letter-spacing: 0.2px;
  }

  .brand {
    position: absolute; left: 50px; top: 59px; width: 122px; height: 58px;
    background: var(--tan); display: flex; align-items: center; justify-content: flex-end; gap: 7px;
    padding-right: 8px;
  }
  .brand-mark { width: 10px; height: 10px; border: 1px solid var(--paper); }
  .brand-name {
    font-family: "Roboto", Arial, sans-serif; font-weight: 300; color: var(--paper);
    font-size: 10.5px; line-height: 13px; letter-spacing: 1.4px; text-align: right;
  }

  .roadmap { position: absolute; left: 0; top: 0; }

  .step-label {
    position: absolute; width: 240px; margin-left: -120px; text-align: center;
    font-weight: 700; font-size: 19px; color: var(--heading);
  }
  .step-text {
    position: absolute; width: 240px; margin-left: -120px; text-align: center;
    font-weight: 300; font-size: 12.8px; line-height: 17.8px; color: var(--body-text);
  }
  .step-text p + p { margin-top: 9px; }

  .testimonials-band { position: absolute; left: 0; top: 680px; width: 1200px; height: 247px; }
  .testimonials-title {
    position: absolute; left: 0; top: 682px; width: 1200px; text-align: center;
    font-weight: 700; font-size: 18.5px; color: var(--heading);
  }
  .testimonial {
    position: absolute; top: 764px; width: 200px; margin-left: -100px; text-align: center;
    font-weight: 400; font-size: 16.4px; line-height: 20.5px; color: var(--paper);
  }
  .testimonial-divider {
    position: absolute; top: 786px; height: 74px; border-left: 2px dashed rgba(255,255,255,0.75);
  }
</style>
</head>
<body>
<div class="page">

  <div class="architecture-backdrop" role="img" aria-label="Faint architectural line drawing of a modern building"></div>

  <svg class="top-band" width="1200" height="70" viewBox="0 0 1200 70">
    <path d="M0 0 H1200 V36 H812 C792 36 786 65 752 65 H448 C414 65 408 36 388 36 H0 Z" fill="var(--tan)"/>
  </svg>
  <h1 class="page-title">NLD Calm Compass</h1>

  <div class="brand">
    <span class="brand-mark"></span>
    <span class="brand-name">NED<br>LINDEN<br>DESIGN</span>
  </div>

  <svg class="roadmap" width="1200" height="680" viewBox="0 0 1200 680" aria-hidden="true">
    <defs>
      <radialGradient id="ringFill" cx="40%" cy="40%" r="65%">
        <stop offset="0%" stop-color="#f3efe7"/>
        <stop offset="70%" stop-color="#d8ccb6"/>
        <stop offset="100%" stop-color="#a89878"/>
      </radialGradient>
      <filter id="softShadow" x="-30%" y="-30%" width="160%" height="160%">
        <feDropShadow dx="0" dy="2" stdDeviation="3" flood-color="#8a7a5c" flood-opacity="0.25"/>
      </filter>
      <g id="stepRing">
        <circle r="66" fill="none" stroke="var(--tan-dark)" stroke-width="1.2" stroke-dasharray="5 4"/>
        <circle r="58" fill="url(#ringFill)" filter="url(#softShadow)"/>
        <circle r="46" cx="-1" cy="-1" fill="var(--paper)"/>
      </g>
    </defs>

    <!-- journey path -->
    <g stroke="var(--tan-dark)" stroke-width="1.2" stroke-dasharray="5 4" fill="none">
      <line x1="190" y1="352" x2="228" y2="376"/>
      <line x1="344" y1="376" x2="384" y2="352"/>
      <line x1="502" y1="352" x2="540" y2="376"/>
      <line x1="656" y1="376" x2="696" y2="352"/>
      <line x1="814" y1="352" x2="852" y2="376"/>
      <line x1="968" y1="376" x2="1008" y2="352"/>
      <!-- connectors to labels -->
      <line x1="130" y1="381" x2="130" y2="436"/>
      <line x1="442" y1="381" x2="442" y2="436"/>
      <line x1="754" y1="381" x2="754" y2="436"/>
      <line x1="1066" y1="381" x2="1066" y2="436"/>
      <line x1="286" y1="293" x2="286" y2="349"/>
      <line x1="598" y1="293" x2="598" y2="349"/>
      <line x1="910" y1="293" x2="910" y2="349"/>
    </g>
    <g fill="var(--tan-dark)">
      <circle cx="130" cy="443" r="8"/>
      <circle cx="442" cy="443" r="8"/>
      <circle cx="754" cy="443" r="8"/>
      <circle cx="1066" cy="443" r="8"/>
      <circle cx="286" cy="286" r="8"/>
      <circle cx="598" cy="286" r="8"/>
      <circle cx="910" cy="286" r="8"/>
    </g>

    <use href="#stepRing" x="130" y="314"/>
    <use href="#stepRing" x="286" y="416"/>
    <use href="#stepRing" x="442" y="314"/>
    <use href="#stepRing" x="598" y="416"/>
    <use href="#stepRing" x="754" y="314"/>
    <use href="#stepRing" x="910" y="416"/>
    <use href="#stepRing" x="1066" y="314"/>

    <!-- listening: ear with sound lines -->
    <g transform="translate(128 314)" fill="var(--icon)">
      <path d="M-22 -4 C-22 -20 -8 -24 0 -20 C8 -16 9 -6 4 2 C0 8 2 14 -4 20 C-10 24 -16 18 -16 12 C-16 6 -22 4 -22 -4 Z" fill="var(--icon-light)"/>
      <path d="M-15 -4 C-15 -14 -4 -15 -2 -8 C0 -2 -6 0 -8 6 C-10 10 -14 8 -14 4 Z"/>
      <g stroke="var(--icon)" stroke-width="3" stroke-linecap="round">
        <line x1="14" y1="-12" x2="24" y2="-17"/>
        <line x1="14" y1="0" x2="26" y2="0"/>
        <line x1="14" y1="12" x2="24" y2="17"/>
      </g>
    </g>

    <!-- visioning: eye -->
    <g transform="translate(286 416)">
      <path d="M-28 0 C-14 -20 14 -20 28 0 C14 20 -14 20 -28 0 Z" fill="var(--icon-light)"/>
      <circle r="13" fill="var(--icon)"/>
      <circle r="7" fill="var(--tan-dark)"/>
      <circle cx="-3" cy="-3" r="3" fill="var(--paper)"/>
    </g>

    <!-- planning: checklist -->
    <g transform="translate(442 314)">
      <rect x="-20" y="-22" width="40" height="46" rx="2" fill="var(--icon-light)"/>
      <g stroke="var(--icon)" stroke-width="3" stroke-linecap="round">
        <line x1="-12" y1="-26" x2="-12" y2="-19"/>
        <line x1="0" y1="-26" x2="0" y2="-19"/>
        <line x1="12" y1="-26" x2="12" y2="-19"/>
        <line x1="-2" y1="-8" x2="14" y2="-8"/>
        <line x1="-2" y1="3" x2="14" y2="3"/>
        <line x1="-2" y1="14" x2="14" y2="14"/>
      </g>
      <g stroke="var(--tan-dark)" stroke-width="1.8" fill="none" stroke-linecap="round">
        <polyline points="-14,-9 -11,-6 -7,-11"/>
        <polyline points="-14,2 -11,5 -7,0"/>
        <polyline points="-14,13 -11,16 -7,11"/>
      </g>
    </g>

    <!-- designing: palette with brush -->
    <g transform="translate(600 416)">
      <circle r="24" fill="var(--icon-light)"/>
      <circle cx="6" cy="8" r="6" fill="var(--paper)"/>
      <g fill="var(--icon)">
        <circle cx="-2" cy="-13" r="4"/>
        <circle cx="10" cy="-10" r="4"/>
        <circle cx="15" cy="2" r="4"/>
        <circle cx="-12" cy="2" r="4"/>
      </g>
      <rect x="-25" y="-24" width="6" height="32" rx="3" fill="var(--icon)"/>
      <path d="M-26 8 H-18 C-18 16 -22 22 -28 24 C-26 18 -27 12 -26 8 Z" fill="var(--tan-dark)"/>
    </g>

    <!-- managing: people around a gear -->
    <g transform="translate(754 314)" fill="var(--icon)">
      <circle r="7" fill="var(--tan-dark)"/>
      <circle r="3" fill="var(--paper)"/>
      <g>
        <circle cx="0" cy="-26" r="4.5"/><path d="M-8 -13 C-8 -20 8 -20 8 -13 Z"/>
        <circle cx="0" cy="17" r="4.5" fill="var(--tan-dark)"/><path d="M-8 30 C-8 23 8 23 8 30 Z" fill="var(--tan-dark)"/>
        <circle cx="-24" cy="-5" r="4.5" fill="var(--tan-dark)"/><path d="M-32 8 C-32 1 -16 1 -16 8 Z"/>
        <circle cx="24" cy="-5" r="4.5" fill="var(--tan-dark)"/><path d="M16 8 C16 1 32 1 32 8 Z"/>
      </g>
      <g stroke="var(--icon-light)" stroke-width="1.6" fill="none">
        <line x1="-16" y1="-17" x2="-10" y2="-22"/>
        <line x1="16" y1="-17" x2="10" y2="-22"/>
        <line x1="-16" y1="16" x2="-10" y2="22"/>
        <line x1="16" y1="16" x2="10" y2="22"/>
      </g>
    </g>

    <!-- installing: document with download arrow -->
    <g transform="translate(910 416)">
      <rect x="-20" y="-24" width="36" height="44" rx="4" fill="var(--icon-light)"/>
      <path d="M-20 20 H26 C26 24 22 26 16 26 H-14 C-18 26 -20 24 -20 20 Z" fill="var(--icon)"/>
      <g stroke="var(--tan-dark)" stroke-width="2.6" fill="none" stroke-linecap="round">
        <line x1="-2" y1="-14" x2="-2" y2="0"/>
        <polyline points="-9,-6 -2,1 5,-6"/>
      </g>
    </g>

    <!-- completing: tick -->
    <g transform="translate(1066 314)">
      <path d="M-26 -2 L-16 -4 L-4 10 L22 -22 L28 -20 L-2 22 Z" fill="var(--tan-dark)"/>
    </g>
  </svg>

  <!-- lower-row labels (steps above the line) -->
  <h2 class="step-label" style="left:286px; top:140px;">Visioning</h2>
  <div class="step-text" style="left:286px; top:171px;">
    <p>Facilitating a guided visioning<br>process to clarify the deepest<br>intention, true purpose, and<br>highest potential for their<br>home and their future within it.</p>
  </div>

  <h2 class="step-label" style="left:598px; top:140px;">Designing</h2>
  <div class="step-text" style="left:598px; top:171px;">
    <p>Following the schedule through the<br>design phases from initial design<br>concepts, technical drawings and<br>details, and the selection of all finishes,<br>fixtures, and surnishings.</p>
  </div>

  <h2 class="step-label" style="left:910px; top:140px;">Installing</h2>
  <div class="step-text" style="left:910px; top:171px;">
    <p>Overseeing the inspection,<br>installation, and arrangement of<br>all furnishings, lighting, artwork,<br>and decorative items.</p>
    <p>Taking care of every last detail.</p>
  </div>

  <!-- upper-row labels (steps below the line) -->
  <h2 class="step-label" style="left:130px; top:456px;">Listening</h2>
  <div class="step-text" style="left:130px; top:488px;">
    <p>Listening to our clients, their<br>land, and their home.</p>
    <p>Identifying their needs,<br>challenges, wishes, and<br>dreams.</p>
  </div>

  <h2 class="step-label" style="left:442px; top:456px;">Planning</h2>
  <div class="step-text" style="left:442px; top:488px;">
    <p>Turning our client's vision<br>into a clearly defined scope.,<br>budget, and timeline.<br>Mapping out the steps for<br>making their dream a reality.<br>Setting a meeting schedule<br>from start to finish.</p>
  </div>

  <h2 class="step-label" style="left:754px; top:456px;">Managing</h2>
  <div class="step-text" style="left:754px; top:488px;">
    <p>Coordinating with clients,<br>builders, architects, and vendors<br>to ensure that the design is<br>executed with excellence, and the<br>construction and furnishings are<br>on-time and on-budget.</p>
  </div>

  <h2 class="step-label" style="left:1066px; top:456px;">Completing</h2>
  <div class="step-text" style="left:1066px; top:488px;">
    <p>Fixing any issues or defects.<br>Follow up on all remaining<br>items.<br>Completing the final finishing<br>touches to our client's full and<br>total satisfaction.</p>
  </div>

  <svg class="testimonials-band" width="1200" height="247" viewBox="0 0 1200 247">
    <path d="M0 12 H495 C512 12 518 34 540 34 H660 C682 34 688 12 705 12 H1200 V247 H0 Z" fill="var(--tan)"/>
  </svg>
  <h2 class="testimonials-title">Testimonials</h2>

  <p class="testimonial" style="left:180px;">Ned to send over testimonials for fill this space - three or four columns of testimonials</p>
  <span class="testimonial-divider" style="left:319px;"></span>
  <p class="testimonial" style="left:459px;">Ned to send over testimonials for fill this space - three or four columns of testimonials</p>
  <span class="testimonial-divider" style="left:599px;"></span>
  <p class="testimonial" style="left:740px;">Ned to send over testimonials for fill this space - three or four columns of testimonials</p>
  <span class="testimonial-divider" style="left:879px;"></span>
  <p class="testimonial" style="left:1019px;">Ned to send over testimonials for fill this space - three or four columns of testimonials</p>

</div>
</body>
</html>
```